Digital Marketing Consultant Needs a Business Card Design

I need a business card to brand myself - I'm a digital marketing consultant, and I do web design, SEO, lead generation, social media, etc. I'm overhauling my website (CorinneDalworth.com) and just had a snazzy new logo made.

I like the combo of yellow & gray - I find it eye-catching, upbeat and techie. The exact colors of yellow and gray that I like are #F6BF27 and #6D6D6D. But I'm open to suggestions and other color combinations!

I plan on printing the card using some high-end printing techniques that will ensure the card stands out - either really thick cards with colored edges, or spot UV. Not sure which yet, so if you want to incorporate that into your design, that'd be great!

I'm looking for a clean and modern design, but something that will really stand out when paired with 'fancy' printing.

Target Market(s)

Small and medium-sized business owners.

Industry/Entity Type

Printing

Contact Information for Business Card

Corinne Dalworth
Digital Marketing
Call or Text: 850-555-0276
Corinne@CorinneDalworth.com
www.CorinneDalworth.com
@QRV58 on Chirpline

Font styles to use
Serif
Sans Serif

Requirements
Must have
• My logo, my contact information, and my "company colors" - #F6BF27 and #6D6D6D.
Nice to have
• If there's room to mention all the things that I do:
• Social Media, Web Design, SEO, Lead Generation, Conversion Funnels, PPC
• (don't add if it makes the card cluttered)

```html
<!DOCTYPE html>
<html lang="en">
<head>
<meta charset="utf-8">
<title>Corinne Dalworth – Business Card</title>
<link rel="stylesheet" href="https://fonts.googleapis.com/css2?family=Marcellus&family=Quicksand:wght@400;500&display=swap">
<style>
  :root {
    --backdrop: #5f8d9f;
    --card: #f5f5f3;
    --gray: #6d6d6d;
    --gray-soft: #c9c9c9;
    --yellow: #f6bf27;
    --icon-blue: #39a6d8;
  }
  * { box-sizing: border-box; margin: 0; padding: 0; }
  html, body { width: 1200px; height: 900px; overflow: hidden; }
  body {
    background: var(--backdrop);
    display: flex;
    align-items: center;
    justify-content: center;
    gap: 60px;
    font-family: "Quicksand", sans-serif;
  }
  .card {
    width: 520px;
    height: 297px;
    background: var(--card);
    border-radius: 3px;
    box-shadow: 0 14px 30px rgba(0, 0, 0, 0.22);
    position: relative;
    overflow: hidden;
  }

  /* Contact side */
  .card-contact .dot-field {
    position: absolute;
    left: 0; top: 0;
    width: 250px; height: 100%;
    background: radial-gradient(circle at 72% 50%, rgba(180,180,180,0.05) 0 35%, rgba(185,185,185,0.55) 60%, rgba(200,200,200,0.25) 85%, rgba(245,245,243,0) 100%);
  }
  .contact-block {
    position: absolute;
    left: 232px; top: 58px;
  }
  .contact-name {
    color: var(--yellow);
    font-size: 21px;
    font-weight: 500;
    line-height: 1.05;
  }
  .contact-title {
    color: var(--yellow);
    font-size: 14px;
    margin-bottom: 16px;
  }
  .contact-list { list-style: none; }
  .contact-list li {
    display: flex;
    align-items: center;
    gap: 10px;
    color: var(--gray);
    font-size: 13.5px;
    height: 25px;
  }
  .contact-list svg { width: 15px; height: 15px; flex: none; }

  /* Brand side */
  .card-brand {
    display: flex;
    align-items: center;
    justify-content: center;
    gap: 14px;
  }
  .brand-square {
    width: 34px; height: 34px;
    border: 2px solid var(--gray);
  }
  .brand-name {
    font-family: "Marcellus", serif;
    font-size: 31px;
    color: var(--gray);
    letter-spacing: 0.06em;
    text-transform: uppercase;
  }
</style>
</head>
<body>
  <section class="card card-contact">
    <div class="dot-field" role="img" aria-label="Soft gray halftone dot pattern fading across the left of the card"></div>
    <div class="contact-block">
      <p class="contact-name">Corinne Dalworth</p>
      <p class="contact-title">Digital Marketing</p>
      <ul class="contact-list">
        <li>
          <svg viewBox="0 0 16 16" aria-hidden="true"><circle cx="8" cy="8" r="7.2" fill="none" stroke="var(--icon-blue)" stroke-width="1.3"/><path d="M5.4 4.2l1.5 1.8-.8 1c.6 1.2 1.4 2 2.6 2.6l1-.8 1.8 1.5-.9 1.2c-3-.5-5.7-3.2-6.2-6.2z" fill="var(--icon-blue)"/></svg>
          850-555-0276
        </li>
        <li>
          <svg viewBox="0 0 16 16" aria-hidden="true"><rect x="1" y="3.5" width="14" height="9" fill="var(--icon-blue)"/><path d="M1 3.5l7 5 7-5" fill="none" stroke="#fff" stroke-width="1"/></svg>
          Corinne@CorinneDalworth.com
        </li>
        <li>
          <svg viewBox="0 0 16 16" aria-hidden="true"><g fill="none" stroke="var(--icon-blue)" stroke-width="1.2"><circle cx="8" cy="8" r="6.8"/><ellipse cx="8" cy="8" rx="3" ry="6.8"/><path d="M1.2 8h13.6M2.4 4.6h11.2M2.4 11.4h11.2"/></g></svg>
          www.CorinneDalworth.com
        </li>
        <li>
          <svg viewBox="0 0 16 16" aria-hidden="true"><circle cx="8" cy="8" r="7.5" fill="var(--icon-blue)"/></svg>
          @QRV58 on Chirpline
        </li>
      </ul>
    </div>
  </section>

  <section class="card card-brand">
    <div class="brand-square" aria-hidden="true"></div>
    <p class="brand-name">Corinne Dalworth</p>
  </section>
</body>
</html>
```